Training Brochure for Local Government Program needs a makeover and some creative design!

We would like our plain and boring brochure updated to be enticing for people to register for this program. Our organisation works in Local Government (Councils) in Australia and we are running our "leadership" program again in 2017.

We would like the brochure for this program to be engaging, bright and modern to entice the future leaders to participate.

The original file was created in Publisher, however we require the final file to be an easily editable PDF with front and back cover for updating in future years and for minor content changes.

It is not intended that this will be printed but made available electronically, however A4 size would be appreciated.

We require the following to be included
Our Logo (Supplied)
KRVN Logo (To be supplied within 48 hours)

Aspiring Leaders in Government
Young business minded people

Government

Serif
Sans Serif
Decorative

Designer to choose colors to be used in the design.

Must have
• Our Logo - Supplied
• The Facilitators logo (KRVN) - Supplied
Nice to have
• Our Corporate colours used
• Some nice photo's or use of icons etc

```html
<!DOCTYPE html>
<html lang="en">
<head>
<meta charset="utf-8">
<title>Emerging Leaders Program 2017</title>
<link href="https://fonts.googleapis.com/css2?family=Lato:wght@400;700;900&display=swap" rel="stylesheet">
<style>
  :root {
    --navy: #0c4262;
    --orange: #e08f0c;
    --green: #4f8a16;
    --ink: #1e1e1e;
    --sage: #6f8c80;
    --red: #d0191f;
    --paper: #ffffff;
    --backdrop: #e9e9e9;
  }
  * { margin: 0; padding: 0; box-sizing: border-box; }
  html, body {
    width: 1200px; height: 1200px; overflow: hidden;
    background: var(--backdrop);
    font-family: "Lato", sans-serif;
  }
  .brochure {
    position: absolute; left: 186px; top: 20px;
    width: 828px; height: 1160px;
    background: var(--paper);
    overflow: hidden;
  }
  .cover-art { position: absolute; left: 0; top: 0; width: 828px; height: 961px; }
  .org-mark {
    position: absolute; left: 524px; top: 52px;
    display: flex; align-items: center; gap: 12px;
    color: var(--green); font-weight: 700; font-size: 22px; line-height: 1.05;
  }
  .org-mark .dot { width: 58px; height: 58px; border-radius: 50%; background: var(--green); flex: none; }
  .title {
    position: absolute; right: 44px; top: 566px;
    color: #fff; font-weight: 900; font-size: 63px; line-height: 74px;
    text-align: right; letter-spacing: -0.5px;
  }
  .intro {
    position: absolute; left: 289px; top: 722px; width: 494px;
    color: #fff; font-size: 16.2px; line-height: 21.2px;
    text-align: justify; text-align-last: right;
  }
  .footer { position: absolute; left: 0; top: 961px; width: 828px; height: 199px; }
  .footer-heading {
    position: absolute; left: 18px; top: 20px;
    color: var(--green); font-weight: 700; font-size: 17.5px;
  }
  .contact-list { position: absolute; left: 56px; top: 59px; list-style: none; }
  .contact-list li {
    display: flex; align-items: flex-start; gap: 12px;
    color: var(--ink); font-size: 16.5px; line-height: 21px; margin-bottom: 9px;
  }
  .contact-list svg { width: 24px; height: 21px; flex: none; }
  .partner-mark {
    position: absolute; left: 432px; top: 58px;
    display: flex; align-items: center; gap: 14px;
    color: var(--sage); font-size: 14px; letter-spacing: 3px; line-height: 22px;
  }
  .partner-mark .dot { width: 96px; height: 96px; border-radius: 50%; background: var(--sage); flex: none; }
  .facilitator-mark {
    position: absolute; left: 706px; top: 118px;
    color: var(--red); font-weight: 700; font-size: 34px; letter-spacing: 1px;
  }
</style>
</head>
<body>
  <main class="brochure">
    <svg class="cover-art" viewBox="0 0 828 961" aria-hidden="false">
      <defs>
        <linearGradient id="photo-tone" x1="0" y1="0" x2="1" y2="1">
          <stop offset="0" stop-color="#cfd3d6"/>
          <stop offset="0.45" stop-color="#eef0f1"/>
          <stop offset="1" stop-color="#b9bcbf"/>
        </linearGradient>
      </defs>
      <rect x="0" y="0" width="828" height="590" fill="url(#photo-tone)" role="img"
            aria-label="Photo of five young professionals in white shirts working together at a meeting table with a laptop"/>
      <polygon class="navy-panel" points="0,583 828,468 828,961 0,961" fill="var(--navy)"/>
      <polygon class="orange-ribbon" points="0,583 218,557 233,711 83,800 229,914 0,799" fill="var(--orange)"/>
    </svg>

    <div class="org-mark">
      <span class="dot"></span>
      <span>Civic Sector<br>Professionals</span>
    </div>

    <h1 class="title">Emerging Leaders<br>Program 2017</h1>

    <p class="intro">This Program, facilitated by Kerravon University, is a unique professional development opportunity for current leaders, those who aspire to positions of leadership and those who aspire to provide leadership in a particular area of interest within the Local Government sector. The Program will focus on equipping emerging leaders with an understanding of the key challenges facing local government in the future; the skills and competencies to develop leadership ability; and the resources to continue learning and practicing leadership behaviours.</p>

    <footer class="footer">
      <h2 class="footer-heading">Civic Sector Professionals Tasmania</h2>
      <ul class="contact-list">
        <li>
          <svg viewBox="0 0 24 21" aria-label="Address"><path d="M12 1a6 6 0 0 0-6 6c0 4.5 6 12 6 12s6-7.5 6-12a6 6 0 0 0-6-6zm0 8.3a2.3 2.3 0 1 1 0-4.6 2.3 2.3 0 0 1 0 4.6z" fill="var(--green)"/></svg>
          <span>PO Box 412 KINGSWELL<br>TAS&nbsp; 7012</span>
        </li>
        <li>
          <svg viewBox="0 0 24 21" aria-label="Phone"><circle cx="12" cy="10.5" r="9.5" fill="none" stroke="var(--green)" stroke-width="1.6"/><path d="M8.6 6.2l1.6-.4 1 2.4-1.1.9a6.5 6.5 0 0 0 2.9 2.9l.9-1.1 2.4 1-.4 1.6c-.2.6-.8 1-1.4.9a8.2 8.2 0 0 1-6.8-6.8c-.1-.6.3-1.2.9-1.4z" fill="var(--green)"/></svg>
          <span>0400 555 182</span>
        </li>
        <li>
          <svg viewBox="0 0 24 21" aria-label="Email"><rect x="3" y="5" width="18" height="12" fill="var(--green)"/><path d="M3 5l9 7 9-7" fill="none" stroke="#fff" stroke-width="1.4"/></svg>
          <span>eo@civicprostas.org.au</span>
        </li>
      </ul>

      <div class="partner-mark">
        <span class="dot"></span>
        <span>COUNCIL<br>MANAGERS<br>NETWORK</span>
      </div>

      <div class="facilitator-mark">KRVN</div>
    </footer>
  </main>
</body>
</html>
```